Defend science flier

Put my name and text below on one side of flier, and place other text on other side. Try to keep file about 4 by 6 or 6 by 8 inches.

Target Market(s)

Community and retailers.

Industry/Entity Type

Retail and concerned community.

Font styles to use
Serif

Requirements
Must have
• Good, eye-catching titles. Be smaller format. Not 8 by 11
Nice to have
• Black and white text. Maybe bullets etc for organizion but no decorations.
Should not have
• Any decoration

```html
<!DOCTYPE html>
<html lang="en">
<head>
<meta charset="utf-8">
<title>Defend Science Flier – Martin R. Holloway</title>
<link rel="stylesheet" href="https://fonts.googleapis.com/css2?family=Tinos:wght@400;700&display=swap">
<style>
  :root {
    --gold: #b59a55;
    --cream: #fbfaf1;
    --paper: #ffffff;
    --ink: #1d1d1d;
    --band-dark: #231f20;
    --quote-grey: #c9c9c9;
    --stage: #ececec;
  }
  * { box-sizing: border-box; margin: 0; padding: 0; }
  html, body {
    width: 800px; height: 1200px; overflow: hidden;
    background: var(--stage);
    font-family: "Tinos", "Times New Roman", serif;
    color: var(--ink);
  }
  .flier {
    position: absolute; left: 181px; width: 438px; height: 584px;
    background: var(--paper);
    box-shadow: 0 2px 10px rgba(0,0,0,.12);
    overflow: hidden;
  }
  .flier--front { top: 8px; }
  .flier--back { top: 608px; }
  .frame {
    position: absolute; left: 14px; right: 14px; top: 11px; bottom: 0;
    border: 1.5px solid var(--gold); border-bottom: none;
    background: var(--cream);
  }
  .abs { position: absolute; left: 0; right: 0; text-align: center; }

  /* front */
  .name { top: 30px; font-size: 28px; letter-spacing: .3px; }
  .tagline { top: 72px; font-size: 15.5px; }
  .divider-art {
    position: absolute; top: 95px; left: 103px; width: 232px; height: 20px;
    background: linear-gradient(90deg, #d9d6cf, #8f8b84 50%, #d9d6cf);
    border-radius: 10px; opacity: .7;
  }
  .claim-band {
    position: absolute; left: 0; right: 0; top: 138px; height: 90px;
    background: var(--gold); color: #fff;
    font-size: 11.3px; line-height: 1.3; text-align: center;
    padding: 10px 54px 0;
  }
  .claim-band p + p { margin-top: 9px; }
  .endorsement {
    top: 245px; padding: 0 42px;
    font-size: 17px; font-weight: 700; line-height: 1.3;
  }
  .quote-box {
    position: absolute; top: 339px; left: 56px; width: 326px; height: 131px;
    border: 1.2px solid var(--gold); border-radius: 12px; background: var(--paper);
    padding: 30px 20px 0;
    font-size: 10.6px; line-height: 1.37; text-align: justify;
  }
  .quote-mark {
    position: absolute; top: 322px; left: 199px; width: 40px; height: 34px;
    background: var(--cream); color: var(--quote-grey);
    font-size: 48px; font-weight: 700; line-height: 48px; text-align: center;
  }
  .footer-band {
    position: absolute; left: 0; right: 0; bottom: 0; height: 79px;
    background: var(--band-dark); text-align: center; padding-top: 9px;
  }
  .footer-lead { color: #fff; font-size: 15.5px; }
  .footer-url { color: var(--gold); font-size: 27px; line-height: 1.15; }

  /* back */
  .headline-top { top: 18px; font-size: 24px; }
  .headline-main { top: 44px; font-size: 31px; font-weight: 700; letter-spacing: .3px; }
  .rule { position: absolute; left: 58px; width: 322px; height: 1px; background: var(--gold); }
  .rule--upper { top: 86px; }
  .rule--lower { top: 129px; }
  .subhead { top: 92px; font-size: 14px; font-weight: 700; line-height: 1.3; }
  .sin-list { position: absolute; top: 146px; left: 54px; right: 40px; list-style: none; }
  .sin-list li {
    position: relative; padding-left: 25px; font-size: 11.3px; line-height: 1.3;
    min-height: 24.6px;
  }
  .sin-num {
    position: absolute; left: 0; top: 0; width: 15px; height: 14px;
    background: var(--gold); color: #fff; border-radius: 3px;
    font-size: 8.5px; line-height: 14px; text-align: center;
  }
  .argument-box {
    position: absolute; top: 291px; left: 54px; width: 336px; height: 203px;
    border: 1.2px solid var(--gold); border-radius: 12px; background: var(--paper);
    padding: 18px 20px 0 22px;
    font-size: 10.6px; line-height: 1.37; text-align: justify;
  }
  .argument-box p + p { margin-top: 11px; }
</style>
</head>
<body>

<section class="flier flier--front">
  <div class="frame"></div>
  <h1 class="abs name">Martin R. Holloway, Ph.D.</h1>
  <p class="abs tagline">“The Architect of Psychology and History”</p>
  <div class="divider-art" role="img" aria-label="Ornamental scroll divider"></div>
  <div class="claim-band">
    <p>Martin’s Bio-Psych has Restructured the Liberal Arts and Sciences—from Genetics to the Fine Arts and Hollywood.</p>
    <p>Museum Catalogues, Better Nonfiction, and Hollywood Films Now Use Martin’s Methods.</p>
  </div>
  <h2 class="abs endorsement">Martin’s Biopsych is endorsed by Dr. E. Warren Leland, professor of psychiatry at Bayfield Medical School, who said:</h2>
  <blockquote class="quote-box">
    Modern sleep and dream research teaches us—as does Martin Holloway’s book Human Nature or Social Sin—that all human activities, including art and politics, are products of the human brain, and that each of us has the privilege and responsibility of using it and communicating its creations.
  </blockquote>
  <div class="quote-mark" aria-hidden="true">“</div>
  <footer class="footer-band">
    <p class="footer-lead">See Martin’s homepage for more details</p>
    <p class="footer-url">www.martin-holloway.org</p>
  </footer>
</section>

<section class="flier flier--back">
  <div class="frame"></div>
  <p class="abs headline-top">WHY DID THE</p>
  <h1 class="abs headline-main">CULTURE CHANGE?</h1>
  <div class="rule rule--upper"></div>
  <p class="abs subhead">During the 1960s, we socialized the<br>Seven Deadly Sins. Therefore:</p>
  <div class="rule rule--lower"></div>
  <ol class="sin-list">
    <li><span class="sin-num">01</span>Pride became “Racism.”</li>
    <li><span class="sin-num">02</span>Lust became “Sexism” and “Gender“ existing “out there.”</li>
    <li><span class="sin-num">03</span>Gluttony became “Consumer Fetishism.”</li>
    <li><span class="sin-num">04</span>Vanity became “Media Images of Beauty.”</li>
    <li><span class="sin-num">05</span>Sloth became The lack of social action: “Are you fighting for diversity?”</li>
  </ol>
  <div class="argument-box">
    <p>This “fight for diversity” inspires attacks against people like Dr. Holloway for asserting any reality principle about human nature.</p>
    <p>These thugs are religious crusaders who ignore the rule of law and try to stop the progress of science. These fanatics go around and give people a “tear-test”—as during the Salem witch trials. Don’t let them take over.</p>
    <p>The educational and culture elites—such as Hollywood—now reject these theological “social sins.” The elites are replacing theology with traditional, human-based sin.</p>
  </div>
  <footer class="footer-band">
    <p class="footer-lead">See Martin’s homepage for more details</p>
    <p class="footer-url">www.martin-holloway.org</p>
  </footer>
</section>

</body>
</html>
```